Professionell und kommunikativ, kommen gerne wieder.
Zielgruppe
Wir transportieren Güter und Waren aller Art rund um die Welt. Hauptsächlich Luftfracht, aber auch per Schiff und an Land. Hauptsächlich richten wir uns damit an Firmenkunden, weniger an Privatkunden. Für unsere neue Website benötigen wir ein Design.
Aufgabenstellung
Wir benötigen ein Webdesign für den Relaunch unserer Website. Unsere Ideen für unsere neue Website haben wir bereits skizziert (Anlage). Diese Mockups bedürfen nun eines Designs.
Dazu ergänzend gelten die folgenden, formalen Vorgaben:
• 1140px breit, gerne auch Ideen für die Darstellung auf Smartphones und Tablets
• Logo links oben
• Navigation oben waagerecht
• Dropdown-Navigation am Desktop, Hamburger für die mobile Navigation
• Verwendung eines Grid-Systems wie Bootstrap
• Mindestschriftgröße für Mengentext: 16px (bei groß ausfallenden Fonts 15px)
Wir haben keine Hausschriftart und keine festgelegten Farben. Wir möchten aber unser Logo weiterverwenden und da bietet es sich natürlich an, auf dem Rot aufzubauen.

```html
<!DOCTYPE html>
<html lang="en">
<head>
<meta charset="utf-8">
<title>Zarvelo – Contact</title>
<link href="https://fonts.googleapis.com/css2?family=Plus+Jakarta+Sans:wght@400;500;600;700&display=swap" rel="stylesheet">
<style>
  :root {
    --brand-red: #c42032;
    --ink: #111418;
    --text-muted: #5b6370;
    --nav-text: #4a5260;
    --border: #d0d5dd;
    --footer-bg: #212427;
    --footer-text: #e9eaec;
    --white: #ffffff;
    --photo-sky: #c9d8e6;
    --photo-containers: #b3583f;
    --map-base: #e4e7ea;
    --badge-accent: #34a853;
  }
  * { box-sizing: border-box; margin: 0; padding: 0; }
  html, body {
    width: 1100px; height: 1200px; overflow: hidden;
    background: var(--white);
    font-family: "Plus Jakarta Sans", Arial, sans-serif;
    color: var(--ink);
  }
  .page { position: relative; width: 1100px; height: 1200px; }

  .topbar {
    height: 27px; background: var(--brand-red); color: var(--white);
    font-size: 12px; display: flex; justify-content: space-between; align-items: center;
    padding: 0 124px;
  }

  .site-header {
    height: 50px; display: flex; align-items: center; justify-content: space-between;
    padding: 0 124px;
  }
  .brand { display: flex; align-items: center; gap: 6px; font-size: 25px; font-weight: 400; color: var(--nav-text); letter-spacing: 0.5px; }
  .brand-dot { width: 14px; height: 14px; border-radius: 50%; background: var(--brand-red); }
  .main-nav { display: flex; align-items: center; gap: 15px; font-size: 12.5px; color: var(--nav-text); }
  .main-nav .active { color: var(--brand-red); }
  .has-caret { display: inline-flex; align-items: center; gap: 6px; }
  .nav-divider { width: 1px; height: 16px; background: var(--border); }
  .quote-btn {
    background: var(--brand-red); color: var(--white); padding: 0 12px; height: 33px;
    display: inline-flex; align-items: center; font-size: 12.5px;
  }

  .contact-section { position: absolute; top: 127px; left: 124px; width: 852px; height: 600px; }
  .contact-form-col { position: absolute; left: 0; top: 0; width: 402px; }
  .contact-title { font-size: 36px; font-weight: 700; letter-spacing: -0.5px; line-height: 1; margin-top: 8px; }
  .contact-intro { margin-top: 18px; font-size: 15px; line-height: 23px; color: var(--text-muted); width: 350px; }

  .field-label { font-size: 10.5px; font-weight: 500; margin-bottom: 6px; display: block; }
  .field { margin-top: 25px; }
  .field-row { display: flex; gap: 24px; margin-top: 32px; }
  .field-row .field { margin-top: 0; width: 189px; }
  .input {
    height: 36px; border: 1px solid var(--border); display: flex; align-items: center;
    padding: 0 12px; font-size: 12px; color: var(--text-muted);
  }
  .input .country { color: var(--ink); display: inline-flex; align-items: center; gap: 4px; margin-right: 12px; }
  .textarea { height: 97px; border: 1px solid var(--border); }
  .consent { margin-top: 20px; display: flex; align-items: center; gap: 10px; font-size: 12px; color: var(--text-muted); }
  .checkbox { width: 15px; height: 15px; border: 1px solid var(--border); border-radius: 4px; }
  .consent u { text-underline-offset: 2px; }
  .send-btn {
    margin-top: 23px; height: 36px; background: var(--brand-red); color: var(--white);
    display: flex; align-items: center; justify-content: center; font-size: 12.5px; font-weight: 500;
  }

  .contact-photo {
    position: absolute; left: 451px; top: 0; width: 401px; height: 596px;
    background: linear-gradient(180deg, var(--photo-sky) 0%, #d6e2ec 30%, var(--photo-containers) 55%, #a24a34 100%);
  }

  .site-footer {
    position: absolute; left: 0; top: 794px; width: 1100px; height: 406px;
    background: var(--footer-bg); color: var(--footer-text);
  }
  .footer-heading { font-size: 15px; font-weight: 600; color: var(--white); margin-bottom: 12px; line-height: 20px; }
  .office { position: absolute; left: 124px; top: 74px; font-size: 12px; line-height: 18px; }
  .office-map { margin-top: 23px; width: 235px; height: 129px; border-radius: 4px; background: var(--map-base); }
  .footer-col { position: absolute; top: 74px; font-size: 12px; }
  .footer-col li { list-style: none; height: 27px; line-height: 18px; }
  .col-nav { left: 590px; }
  .col-services { left: 736px; }
  .col-legal { left: 882px; }
  .rating-badge {
    position: absolute; left: 841px; top: 232px; width: 135px; height: 58px;
    background: var(--white); border-top: 2px solid var(--badge-accent); border-radius: 2px;
  }
  .copyright { position: absolute; left: 0; right: 0; top: 373px; text-align: center; font-size: 12px; color: #c9ccd1; }
</style>
</head>
<body>
<div class="page">
  <div class="topbar">
    <span>Tel: +49 61234 98765 (call us anytime)</span>
    <span>info@zarvelo-freight.de</span>
  </div>

  <header class="site-header">
    <div class="brand">ZARVELO <span class="brand-dot"></span></div>
    <nav class="main-nav">
      <span>Home</span>
      <span class="has-caret">Services
        <svg width="8" height="5" viewBox="0 0 8 5"><path d="M1 1l3 3 3-3" fill="none" stroke="currentColor" stroke-width="1"/></svg>
      </span>
      <span>About Us</span>
      <span class="active">Contact</span>
      <span class="nav-divider"></span>
      <span class="has-caret">US
        <svg width="8" height="5" viewBox="0 0 8 5"><path d="M1 1l3 3 3-3" fill="none" stroke="currentColor" stroke-width="1"/></svg>
      </span>
      <span class="quote-btn">Get a quote</span>
    </nav>
  </header>

  <main class="contact-section">
    <div class="contact-form-col">
      <h1 class="contact-title">Contact</h1>
      <p class="contact-intro">Would you like to get to know us or do you have a question? You can send us a message using the following form.</p>

      <div class="field-row">
        <div class="field"><span class="field-label">First name</span><div class="input">First name</div></div>
        <div class="field"><span class="field-label">Last name</span><div class="input">Last name</div></div>
      </div>
      <div class="field"><span class="field-label">Email</span><div class="input">you@company.com</div></div>
      <div class="field"><span class="field-label">Phone number</span>
        <div class="input"><span class="country">US
          <svg width="9" height="5" viewBox="0 0 9 5"><path d="M1 0.5l3.5 3.5 3.5-3.5" fill="none" stroke="currentColor" stroke-width="1"/></svg></span>+1 (555) 000-0000</div>
      </div>
      <div class="field"><span class="field-label">Message</span><div class="textarea"></div></div>
      <div class="consent"><span class="checkbox"></span><span>You agree to our friendly <u>privacy policy.</u></span></div>
      <div class="send-btn">Send message</div>
    </div>

    <div class="contact-photo" role="img" aria-label="Cargo plane flying over stacked shipping containers"></div>
  </main>

  <footer class="site-footer">
    <div class="office">
      <h3 class="footer-heading">Our Office</h3>
      <p>Zarvelo GmbH<br>Hafenring 14 60999 Feldstadt</p>
      <div class="office-map" role="img" aria-label="Map of the office location"></div>
    </div>
    <div class="footer-col col-nav">
      <h3 class="footer-heading">Navigation</h3>
      <ul><li>Home</li><li>Services</li><li>About Us</li><li>Contact</li></ul>
    </div>
    <div class="footer-col col-services">
      <h3 class="footer-heading">Services</h3>
      <ul><li>Air Freight</li><li>Sea Freight</li><li>Land Transport</li><li>Airland Services</li></ul>
    </div>
    <div class="footer-col col-legal">
      <h3 class="footer-heading">Legal</h3>
      <ul><li>Legal Notice</li><li>Term of Use</li><li>Privacy Statement</li></ul>
    </div>
    <div class="rating-badge" role="img" aria-label="Customer rating badge"></div>
    <p class="copyright">© 2023 Zarvelo. All Rights Reserved.</p>
  </footer>
</div>
</body>
</html>
```